Nimbo58.com.au Website and company image design

We are looking for an exceptional website designer / company to work with our new Australian Hosting Company

Nimbo58 is a new Cloud Hosting company launching in Australia that provides Scalable, On Demand computing resources to the Australian Market Place. Scalable, On Demand ocmputing is a nice way of saying fully scalable / redundant Virtual Private Server.

We require a full company image to be developed along with a Logo and Website. There is scope for ongoing development (preferred) for the successful candidate.

Website developement will require extensive jQuery ability (sliders for ordering etc (see: http://www.hostrix-example.com.au/virtual-dedicated-servers/253/zar_vps.html).

Please communicate directly with me to establish full website scope and request further documentation / content.

Target Market(s)

Website Designers, programmers, technicians and large companies

Industry/Entity Type

It Company

Requirements
Must have
• Slider ordering system such as http://www.hostrix-example.com.au/virtual-dedicated-servers/253/zar_vps.html

Nice to have
• CMS backend system
Should not have
• Should NOT be a monster template copy!!!

```html
<!DOCTYPE html>
<html lang="en">
<head>
<meta charset="utf-8">
<title>Nimbo58 — Cloud Hosting</title>
<link rel="stylesheet" href="https://fonts.googleapis.com/css2?family=Roboto+Condensed:wght@400;700&family=Arimo:wght@400;700&display=swap">
<style>
:root{
  --ink:#222;
  --text:#555;
  --muted:#8a8a8a;
  --brand:#1a72b9;
  --brand-deep:#0e5a9c;
  --lime:#9cc61a;
  --lime-deep:#6f9a0b;
  --bar:#222;
  --bar-line:#3a3a3a;
  --page:#f4f4f4;
  --footer:#1f1f1f;
  --footer-text:#7d7d7d;
  --footer-head:#4c9ad8;
}
*{box-sizing:border-box;margin:0;padding:0}
html,body{width:1081px;height:1200px;overflow:hidden;background:var(--page)}
body{font-family:"Arimo",Arial,sans-serif;color:var(--text)}
.page{width:1000px;height:1110px;transform:scale(1.081);transform-origin:0 0;position:relative;background:var(--page);overflow:hidden}
.heading{font-family:"Roboto Condensed",Arial,sans-serif}

/* nav */
.topnav{position:absolute;top:0;left:0;width:1000px;height:29px;background:var(--bar);display:flex;justify-content:center}
.topnav ul{display:flex;list-style:none}
.topnav li{border-left:1px solid var(--bar-line);padding:0 12px;line-height:29px;font-size:11px;color:#eee}
.topnav li:last-child{border-right:1px solid var(--bar-line)}

.masthead{position:absolute;top:29px;left:0;width:1000px;height:50px;background:#fff}
.logo{position:absolute;left:148px;top:22px;display:flex;align-items:center;gap:7px;font-family:"Roboto Condensed",Arial,sans-serif;font-weight:700;font-size:28px;line-height:32px;color:var(--brand)}
.logo i{width:12px;height:12px;background:var(--brand);display:block}
.account{position:absolute;right:148px;top:9px;font-size:9px;color:var(--ink)}
.account span{margin-left:14px}

/* hero */
.hero{position:absolute;top:56px;left:0;width:1000px;height:320px}
.hero svg.band{position:absolute;inset:0}
.hero .art{position:absolute;border-radius:6px}
.servers{left:160px;top:68px;width:130px;height:180px;background:linear-gradient(90deg,#111,#333 40%,#1a4f86 55%,#111)}
.device{left:636px;top:70px;width:214px;height:210px;background:radial-gradient(circle at 50% 30%,#cfe8fb,#5aa3df 55%,rgba(40,90,140,0) 75%)}
.arrow{position:absolute;top:160px}
.hero h1{position:absolute;left:348px;top:60px;font-size:23px;line-height:34px;color:#1b2a38;font-weight:700;white-space:nowrap}
.hero h1 b{color:var(--lime);font-size:32px;margin-left:6px}
.perks{position:absolute;left:348px;top:99px;list-style:none;font-size:12px;color:#16324d}
.perks li{height:17px;display:flex;align-items:center;gap:5px;white-space:nowrap}
.perks li::before{content:"";width:8px;height:8px;border-radius:50%;background:var(--lime)}
.btn{position:absolute;top:190px;height:26px;width:87px;line-height:26px;text-align:center;white-space:nowrap;font-family:"Roboto Condensed",Arial,sans-serif;font-size:13px;font-weight:700;border-radius:2px}
.btn-how{left:368px;background:linear-gradient(#a8d21f,var(--lime-deep));color:#fff}
.btn-sign{left:465px;background:linear-gradient(#3a3a3a,#151515);color:#3fa2ef}
.search{position:absolute;left:370px;top:244px;display:flex;height:23px;font-size:10px}
.search .field{width:129px;background:#fff;line-height:23px;padding-left:6px;color:#333}
.search .tld{width:45px;background:var(--lime);color:#1b2a10;line-height:23px;text-align:center;font-weight:700}
.search .go{margin-left:3px;width:45px;background:#222;color:#fff;line-height:23px;text-align:center;font-size:11px}

/* plans */
.section-title{position:absolute;font-family:"Roboto Condensed",Arial,sans-serif;font-weight:700;color:var(--brand);font-size:17px;line-height:20px}
.plans-title{left:149px;top:355px;padding-bottom:6px;border-bottom:1px dotted #aaa;width:134px}
.plans{position:absolute;left:149px;top:409px;width:702px;height:288px;display:flex}
.plan{width:176px;height:288px;position:relative;background:linear-gradient(90deg,#d9d9d9,#efefef 45%,#e2e2e2);border-right:1px solid #ccc}
.plan-head{height:88px;background:#1d1d1d;text-align:center;color:#fff;overflow:hidden}
.plan-name{font-family:"Roboto Condensed",Arial,sans-serif;font-weight:700;font-size:14px;height:26px;line-height:26px;background:#111}
.price{height:62px;line-height:62px;font-family:"Roboto Condensed",Arial,sans-serif;color:#3aa0ea;font-size:40px;background:linear-gradient(#2a2a2a,#1a1a1a);white-space:nowrap}
.price sup{font-size:18px;line-height:0;vertical-align:baseline;position:relative;top:-16px}
.price small{font-size:15px}
.features{list-style:none;font-size:9px;color:#222;padding-top:1px}
.features li{height:28px;line-height:28px;padding-left:30px;position:relative;white-space:nowrap}
.features li::before{content:"›";position:absolute;left:12px;color:#777}
.cart{position:absolute;left:29px;top:266px;width:117px;height:19px;border-radius:3px;background:linear-gradient(#3a3a3a,#111);color:#fff;font-size:9px;line-height:19px;padding-left:30px}
.cart::after{content:"»";position:absolute;right:10px;top:0;line-height:17px;font-size:16px;color:var(--lime)}
.plan.featured{margin-top:-9px;height:306px;background:linear-gradient(90deg,#e4e4e4,#f4f4f4 45%,#e8e8e8);box-shadow:0 2px 12px rgba(0,0,0,.45);z-index:2}
.plan.featured .plan-head{height:97px}
.plan.featured .price{height:71px;line-height:71px;background:linear-gradient(#3ea0e6,#1468b4);color:var(--lime)}
.plan.featured .cart{top:275px}
.plan.featured .cart::after{color:#3aa0ea}

/* info */
.info{position:absolute;top:732px;width:335px;font-size:8px;line-height:13px;color:#555}
.info h2{font-family:"Roboto Condensed",Arial,sans-serif;color:var(--brand);font-size:17px;line-height:20px;margin-bottom:4px}
.info-left{left:148px}
.info-right{left:514px}
.divider{position:absolute;left:496px;top:735px;width:1px;height:150px;background:#ddd}
.ticks{list-style:none;margin-top:5px}
.ticks li{height:18.3px;display:flex;align-items:center;gap:7px;color:#222;white-space:nowrap}
.ticks svg{flex:none}
.info p+p{margin-top:8px}
.quote{margin-top:14px;display:flex;gap:6px;font-size:9.5px;line-height:14px;color:#666}
.quote b{font-size:30px;color:#bbb;line-height:22px;font-family:Georgia,serif}
.quote span{width:285px}

/* footer */
.footer{position:absolute;top:910px;left:0;width:1000px;height:160px;background:var(--footer)}
.fcol{position:absolute;top:12px;font-size:9px;line-height:14.8px;color:var(--footer-text);white-space:nowrap}
.fcol h3{font-size:10px;color:var(--footer-head);margin-bottom:6px}
.fcol ul{list-style:none}
.fcol li::before{content:"› ";color:#aaa}
.fsep{position:absolute;top:15px;width:1px;height:130px;background:#2e2e2e}
.social li{height:20px;display:flex;align-items:center;gap:6px;color:#aaa;font-weight:700}
.social li::before{content:"";width:11px;height:11px;background:#555}
.contact p{color:#888}
.contact b{color:#bbb}
.copyright{position:absolute;top:1070px;width:1000px;height:40px;line-height:36px;text-align:center;font-size:9px;color:#333;background:#f4f4f4}
</style>
</head>
<body>
<div class="page">
  <nav class="topnav"><ul>
    <li>Home</li><li>Domains</li><li>Web Hosting</li><li>Virtual Servers</li><li>Dedicated Servers</li><li>Resellers</li><li>About Us</li><li>Support</li>
  </ul></nav>

  <header class="masthead">
    <div class="logo"><i></i>Nimbo58</div>
    <div class="account">Call: 555-010-2468 <span>Login / Sign Up</span></div>
  </header>

  <section class="hero">
    <svg class="band" width="1000" height="320" viewBox="0 0 1000 320">
      <defs>
        <linearGradient id="sky" x1="0" y1="0" x2="0" y2="1">
          <stop offset="0" stop-color="#3a97dc"/><stop offset="1" stop-color="#176cbd"/>
        </linearGradient>
      </defs>
      <path d="M0 40 C200 40 300 60 380 30 C450 5 600 2 1000 5 L1000 290 C700 290 600 280 480 300 C400 314 300 290 0 283 Z" fill="url(#sky)"/>
      <path d="M0 36 C200 36 300 52 380 24 C450 0 600 -2 1000 1" fill="none" stroke="#1a72b9" stroke-width="4"/>
      <path d="M0 288 C300 292 400 318 480 306 C600 288 700 296 1000 296" fill="none" stroke="#1a72b9" stroke-width="4"/>
      <path d="M0 295 C300 300 400 324 480 313 C600 296 700 304 1000 304" fill="none" stroke="#cfe2f2" stroke-width="2"/>
    </svg>
    <div class="art servers" role="img" aria-label="Illustration of glowing rack servers"></div>
    <div class="art device" role="img" aria-label="Illustration of a cloud sending app icons to a tablet"></div>
    <svg class="arrow" style="left:118px" width="24" height="90" viewBox="0 0 24 90"><path d="M22 2 L4 45 L22 88" fill="none" stroke="#a9cfee" stroke-width="2"/></svg>
    <svg class="arrow" style="left:858px" width="24" height="90" viewBox="0 0 24 90"><path d="M2 2 L20 45 L2 88" fill="none" stroke="#a9cfee" stroke-width="2"/></svg>
    <h1 class="heading">Virtual Private Servers<b>$9.90</b></h1>
    <ul class="perks">
      <li>Unlimited Hosting Space</li><li>Unlimited Monthly Bandwidth</li><li>Host Unlimited Domains</li><li>Free Domain Host for Life</li>
    </ul>
    <div class="btn btn-how">How it Works</div>
    <div class="btn btn-sign">Sign Up Now</div>
    <div class="search"><div class="field">Domain Search....</div><div class="tld">.com ▾</div><div class="go">Search</div></div>
  </section>

  <h2 class="section-title plans-title">Choose Your Plan</h2>
  <section class="plans">
    <article class="plan">
      <div class="plan-head"><div class="plan-name">Bronze Cloud</div><div class="price"><sup>$</sup>30<small>/MO</small></div></div>
      <ul class="features"><li>10 Websites Cap</li><li>5TB Bandwidth Cap</li><li>80GB Space Storage</li><li>Domain Name Included</li><li>24/7 Unlimited Support</li><li>24/7 Unlimited Support</li></ul>
      <div class="cart">Add to Cart</div>
    </article>
    <article class="plan featured">
      <div class="plan-head"><div class="plan-name">Silver Cloud</div><div class="price"><sup>$</sup>49<small>/MO</small></div></div>
      <ul class="features"><li>10 Websites Cap</li><li>5TB Bandwidth Cap</li><li>80GB Space Storage</li><li>Domain Name Included</li><li>24/7 Unlimited Support</li><li>24/7 Unlimited Support</li></ul>
      <div class="cart">Add to Cart</div>
    </article>
    <article class="plan">
      <div class="plan-head"><div class="plan-name">Gold Cloud</div><div class="price"><sup>$</sup>60<small>MO</small></div></div>
      <ul class="features"><li>10 Websites Cap</li><li>5TB Bandwidth Cap</li><li>80GB Space Storage</li><li>Domain Name Included</li><li>24/7 Unlimited Support</li><li>24/7 Unlimited Support</li></ul>
      <div class="cart">Add to Cart</div>
    </article>
    <article class="plan">
      <div class="plan-head"><div class="plan-name">Platimum Cloud</div><div class="price"><sup>$</sup>79<small>/MO</small></div></div>
      <ul class="features"><li>10 Websites Cap</li><li>5TB Bandwidth Cap</li><li>80GB Space Storage</li><li>Domain Name Included</li><li>24/7 Unlimited Support</li><li>24/7 Unlimited Support</li></ul>
      <div class="cart">Add to Cart</div>
    </article>
  </section>

  <section class="info info-left">
    <h2>Cloud Hosting Benefits</h2>
    <p>Lorem Ipsum is simply dummy text of the printing and typesetting industry. Lorem Ipsum has been the industry's standard dummy text ever since the 1500s, when an unknown printer took a galley of type and scrambled it to make a type specimen book.</p>
    <ul class="ticks">
      <li><svg width="13" height="11" viewBox="0 0 13 11"><path d="M1 6 L5 10 L12 1" fill="none" stroke="#5fa21a" stroke-width="2.5"/></svg>It has survived not only five centuries, but also the leap into elec-</li>
      <li><svg width="13" height="11" viewBox="0 0 13 11"><path d="M1 6 L5 10 L12 1" fill="none" stroke="#5fa21a" stroke-width="2.5"/></svg>Tronic typesetting, remaining essentially unchanged. It was popular-</li>
      <li><svg width="13" height="11" viewBox="0 0 13 11"><path d="M1 6 L5 10 L12 1" fill="none" stroke="#5fa21a" stroke-width="2.5"/></svg>Ised in the 1960s with the release of Typesheet sheets containing</li>
      <li><svg width="13" height="11" viewBox="0 0 13 11"><path d="M1 6 L5 10 L12 1" fill="none" stroke="#5fa21a" stroke-width="2.5"/></svg>Lorem Ipsum passages, and more recently with desktop publishing</li>
      <li><svg width="13" height="11" viewBox="0 0 13 11"><path d="M1 6 L5 10 L12 1" fill="none" stroke="#5fa21a" stroke-width="2.5"/></svg>Software like Quill PageSetter including versions of Lorem Ipsum.</li>
    </ul>
  </section>
  <div class="divider"></div>
  <section class="info info-right">
    <h2>Speed &amp; Performance</h2>
    <p>Lorem Ipsum is simply dummy text of the printing and typesetting industry. Lorem Ipsum has been the industry's standard dummy text ever since the 1500s, when an unknown printer took a galley of type and scrambled it to make a type specimen book.</p>
    <p>It is a long established fact that a reader will be distracted by the readable content of a page when looking at its layout. The point of using Lorem Ipsum is that it has a more-or-less normal distribution of letters, as opposed to using 'Content here, content here',</p>
    <div class="quote"><b>“</b><span>It is a long established fact that a reader will be distracted by the readable content of a page when looking at its layout.</span></div>
  </section>

  <footer class="footer">
    <div class="fcol" style="left:149px"><h3>Why Nimbo58</h3><ul><li>Lorem Ipsum is simply</li><li>Dummy text of the printing</li><li>And typesetting industry.</li><li>Lorem Ipsum has been</li><li>the Industry's standard</li><li>dummy Text ever since the</li><li>1500s, When an unknown</li><li>printer Took a galley</li></ul></div>
    <div class="fsep" style="left:285px"></div>
    <div class="fcol" style="left:307px"><h3>Web Hosting</h3><ul><li>Lorem Ipsum is simply</li><li>Dummy text of the printing</li><li>And typesetting industry.</li><li>Lorem Ipsum has been</li><li>the Industry's standard</li><li>dummy Text ever since the</li><li>1500s, When an unknown</li><li>printer Took a galley</li></ul></div>
    <div class="fsep" style="left:444px"></div>
    <div class="fcol" style="left:465px"><h3>Products &amp; Services</h3><ul><li>Lorem Ipsum is simply</li><li>Dummy text of the printing</li><li>And typesetting industry.</li><li>Lorem Ipsum has been</li><li>the Industry's standard</li><li>dummy Text ever since the</li><li>1500s, When an unknown</li><li>printer Took a galley</li></ul></div>
    <div class="fsep" style="left:602px"></div>
    <div class="fcol social" style="left:625px"><h3>Follow Us</h3><ul><li>Friendnet</li><li>WorkLink</li><li>Chirper</li><li>Searchly +</li><li>Callwave</li></ul></div>
    <div class="fsep" style="left:717px"></div>
    <div class="fcol contact" style="left:739px"><h3>Contact</h3><p><b>Call:</b> 555-010-2468</p><p style="margin-top:4px;line-height:12.5px">18 Harbour Lane Eastport,<br>NS 20417<br>AUS</p></div>
  </footer>
  <div class="copyright">Copyright © 2012-2013 Nimbo58. All Rights Reserved | Privacy | Sitmap</div>
</div>
</body>
</html>
```